Quellix Google Display Ad designs

Need two designs one for our Tampa, Fl office and one for our NJ office. Needs to modernly and clearly display that we are a local cloud business phone system provider. Tagline for Tampa design should be "Finally, a Tampa Cloud Phone System Provider" and would like the dorrin archway bridge in that ad.
Second ad tagline should be "Finally, a New Jersey Cloud Phone System Provider" and have a morcott loaf egg and cheese on a roll in the image.

Both ads should have our phones/portal image as attached below

Images of Dorrin Archway and Morcott Loaf egg and cheese attached are just suggestions, feel free to use your own image that looks best

Need 4 sizes of each ad:

300x50
300x250
240x400
200x200

Ive also attached a bramlo ad, i like the top corner where it peels back. If theres room id like it to say "Send us your phone bill for a free cost analysis"

Also, should have a Sign up now button

Business owners and IT directors

Telecommunications

• Modern sleek design

```html
<!DOCTYPE html>
<html lang="en">
<head>
<meta charset="utf-8">
<title>Quellix Display Ads – Tampa</title>
<link rel="stylesheet" href="https://fonts.googleapis.com/css2?family=Oswald:wght@300;500;600&family=Open+Sans:wght@400&display=swap">
<style>
  :root {
    --board: #d1d2d4;
    --purple: #672d8f;
    --orange: #f79c3c;
    --white: #ffffff;
    --ink: #231f20;
    --lavender: #e2d6ee;
    --sky-top: #26207a;
    --sky-mid: #4d3897;
    --sky-low: #6d4f92;
    --water: #17122e;
  }
  * { box-sizing: border-box; margin: 0; padding: 0; }
  html, body {
    width: 1200px; height: 707px; overflow: hidden;
    background: var(--board);
  }
  .board { position: relative; width: 1200px; height: 707px; }
  .size-label {
    position: absolute;
    font: 400 13px/1 "Open Sans", Arial, sans-serif;
    color: #000;
  }
  .ad { position: absolute; overflow: hidden; background: var(--white); }
  .ad > svg.shapes { position: absolute; inset: 0; }
  .logo {
    position: absolute; display: flex; align-items: center; gap: 0.3em;
    font-family: "Oswald", sans-serif; font-weight: 500;
    color: var(--ink); letter-spacing: 0.04em; line-height: 1;
  }
  .logo-dot { width: 0.75em; height: 0.75em; border-radius: 50%; background: var(--purple); }
  .device-shot {
    position: absolute; border-radius: 6px;
    background: linear-gradient(135deg, #f4f5f7 0%, #cfd3d9 55%, #3a3d44 100%);
    box-shadow: 0 4px 10px rgba(0,0,0,0.25);
  }
  .headline {
    position: absolute; font-family: "Oswald", sans-serif; font-weight: 600;
    color: var(--white); line-height: 1; letter-spacing: 0.03em;
  }
  .accent-rule { position: absolute; background: var(--orange); }
  .subline {
    position: absolute; font-family: "Oswald", sans-serif; font-weight: 300;
    color: var(--lavender); text-transform: uppercase;
  }
  .subline strong { font-weight: 500; color: var(--white); }
  .align-right { text-align: right; }
  .cta {
    position: absolute; display: flex; align-items: center; justify-content: center;
    background: var(--orange); color: var(--white);
    font-family: "Oswald", sans-serif; font-weight: 400; text-transform: uppercase;
    clip-path: polygon(8% 0, 100% 0, 92% 100%, 0 100%);
    text-shadow: 0 1px 2px rgba(0,0,0,0.2);
  }
</style>
</head>
<body>
<div class="board">
  <svg width="0" height="0" style="position:absolute">
    <defs>
      <linearGradient id="bridgeNight" x1="0" y1="0" x2="0" y2="1">
        <stop offset="0" stop-color="var(--sky-top)"/>
        <stop offset="0.5" stop-color="var(--sky-mid)"/>
        <stop offset="0.78" stop-color="var(--sky-low)"/>
        <stop offset="1" stop-color="var(--water)"/>
      </linearGradient>
    </defs>
  </svg>

  <!-- 240x400 -->
  <div class="size-label" style="left:66px;top:65px">240x400</div>
  <div class="ad ad-skyscraper" style="left:66px;top:86px;width:324px;height:539px;background:var(--purple)">
    <svg class="shapes" width="324" height="539" viewBox="0 0 324 539">
      <polygon points="0,0 180,0 0,156" fill="var(--white)"/>
      <line x1="196" y1="258" x2="324" y2="336" stroke="var(--white)" stroke-width="7"/>
      <g role="img" aria-label="Dorrin Archway bridge lit up at night over the bay">
        <path d="M162,0 L324,0 L324,330 L82,190 Q62,178 74,158 Z" fill="url(#bridgeNight)"/>
      </g>
    </svg>
    <div class="logo" style="left:16px;top:36px;font-size:22px"><span class="logo-dot"></span>QUELLIX</div>
    <div class="device-shot" role="img" aria-label="Desk phones, laptop, monitor and mobile showing the phone portal" style="left:30px;top:203px;width:200px;height:98px"></div>
    <div class="headline" style="left:33px;top:323px;font-size:34px">FINALLY,</div>
    <div class="accent-rule" style="left:34px;top:362px;width:52px;height:3px"></div>
    <div class="subline" style="left:33px;top:366px;font-size:28px;line-height:33px">A <strong>Tampa</strong> Cloud Phone<br>System Provider</div>
    <div class="cta" style="left:55px;top:459px;width:201px;height:48px;font-size:22px">Sign up now</div>
  </div>

  <!-- 300x50 -->
  <div class="size-label" style="left:417px;top:113px">300x50</div>
  <div class="ad ad-banner" style="left:417px;top:149px;width:405px;height:67px">
    <svg class="shapes" width="405" height="67" viewBox="0 0 405 67">
      <polygon points="88,0 300,0 336,67 120,67" fill="var(--purple)"/>
      <g role="img" aria-label="Dorrin Archway bridge at night">
        <polygon points="0,0 83,0 116,67 0,67" fill="url(#bridgeNight)"/>
      </g>
    </svg>
    <div class="headline" style="left:124px;top:14px;font-size:14px">FINALLY,</div>
    <div class="subline" style="left:124px;top:28px;font-size:10.5px;line-height:12px">A <strong>Tampa</strong> Cloud Phone<br>System Provider</div>
    <div class="device-shot" role="img" aria-label="Phones and screens showing the phone portal" style="left:215px;top:12px;width:72px;height:40px;border-radius:3px"></div>
    <div class="logo" style="left:344px;top:12px;font-size:12px"><span class="logo-dot"></span>QUELLIX</div>
    <div class="cta" style="left:287px;top:33px;width:104px;height:25px;font-size:11px">Sign up now</div>
  </div>

  <!-- 300x250 -->
  <div class="size-label" style="left:417px;top:259px">300x250</div>
  <div class="ad ad-rectangle" style="left:417px;top:288px;width:405px;height:337px">
    <svg class="shapes" width="405" height="337" viewBox="0 0 405 337">
      <path d="M287,0 L405,0 L405,337 L250,337 L132,122 Q122,104 140,92 Z" fill="var(--purple)"/>
      <g role="img" aria-label="Dorrin Archway bridge lit up at night over the bay">
        <path d="M0,40 Q0,10 32,10 L59,10 L233,337 L0,337 Z" fill="url(#bridgeNight)"/>
      </g>
    </svg>
    <div class="logo" style="left:97px;top:22px;font-size:18px"><span class="logo-dot"></span>QUELLIX</div>
    <div class="device-shot" role="img" aria-label="Desk phones, laptop, monitor and mobile showing the phone portal" style="left:232px;top:40px;width:160px;height:80px"></div>
    <div class="headline align-right" style="right:13px;top:146px;font-size:34px">FINALLY,</div>
    <div class="accent-rule" style="right:13px;top:184px;width:36px;height:3px"></div>
    <div class="subline align-right" style="right:13px;top:188px;font-size:25px;line-height:27px">A <strong>Tampa</strong> Cloud Phone<br>System Provider</div>
    <div class="cta" style="left:253px;top:279px;width:132px;height:31px;font-size:15px">Sign up now</div>
  </div>

  <!-- 200x200 -->
  <div class="size-label" style="left:851px;top:329px">200x200</div>
  <div class="ad ad-square" style="left:851px;top:356px;width:270px;height:269px">
    <svg class="shapes" width="270" height="269" viewBox="0 0 270 269">
      <path d="M232,0 L270,0 L270,269 L201,269 L110,96 Q102,80 118,72 Z" fill="var(--purple)"/>
      <g role="img" aria-label="Dorrin Archway bridge lit up at night">
        <path d="M0,28 Q0,4 26,4 L52,4 L194,269 L0,269 Z" fill="url(#bridgeNight)"/>
      </g>
    </svg>
    <div class="logo" style="left:84px;top:16px;font-size:14px"><span class="logo-dot"></span>QUELLIX</div>
    <div class="device-shot" role="img" aria-label="Desk phones, laptop, monitor and mobile showing the phone portal" style="left:147px;top:54px;width:118px;height:60px"></div>
    <div class="headline align-right" style="right:9px;top:126px;font-size:22px">FINALLY,</div>
    <div class="accent-rule" style="right:9px;top:152px;width:32px;height:2px"></div>
    <div class="subline align-right" style="right:9px;top:157px;font-size:14px;line-height:15px">A <strong>Tampa</strong> Cloud Phone<br>System Provider</div>
    <div class="cta" style="left:127px;top:216px;width:132px;height:32px;font-size:14px">Sign up now</div>
  </div>
</div>
</body>
</html>
```